New Hotel Showcase Website

We plan to launch a website called www.fernlodgings.net which showcases the world’s best new hotels. We want a mock up for 2 pages: the homepage (page 1) and the individual hotel page (page 2). We are looking for a design which combines simplicity while highlighting images/features of the hotel. Because the theme of the site is new hotels it is important that the design somehow emphasizes the age of each hotel listed – both on the homepage and then on the individual hotel page.

NOTE: WE WANT A CREATIVE, NEW APPROACH TO DISPLAYING HOTELS. NOT JUST A COPY OF CURRENT HOTEL WEBSITES.

The design should consider unique and creative ways of helping users to navigate the homepage (page 1) based on the age, location or style of the hotel they are interested in. The individual hotel page(page 2) can be more standard by clearly setting out hotel photos, feature lists, reviews, contact details and potential discounts. There is no booking system needed as this is not a hotel booking website.

The design should ideally be compatible with a content management system such as Page Forge. In terms of reference materials we like sites similar to:

http://www.quillwanderer.net
http://www.bobandkayporter.net
http://www.craftinns.net
http://www.pebblestays.net

These sites are designed far more simply than large booking sites such as www.voyaro.net, www.roomsy.net or even jaunt ledger. However, we are not looking for a copy of the above. We are looking for a design that presents hotels in a novel way and would be seen by the industry as a unique way of displaying new hotels.
Updates

Dear Designers - we have received quite a few entries already. Thank you. However, none of the designs submitted have responded to our brief. They are all copies or derivatives of current hotel websites which is not what we are looking for. We want (a) a new and creative approach to a hotel website and (b) one which creatively uses the age of the hotel (ie. 1 month old, 6 months old etc).

It will require creative thinking and new ideas. We wanted to challenge designers to come up with something new. Thanks.

```html
<!DOCTYPE html>
<html lang="en">
<head>
<meta charset="utf-8">
<title>Fern Lodgings – New Hotels</title>
<link rel="stylesheet" href="https://fonts.googleapis.com/css2?family=PT+Sans:wght@400;700&family=Roboto+Condensed:wght@300;400&family=Noto+Serif:wght@400&display=swap">
<style>
:root{
  --page:#f2f2f2;
  --blue:#1aa1dc;
  --blue-light:#28b1ea;
  --ink:#222;
  --bar:#262a2d;
  --footer:#232527;
  --footer-base:#101112;
  --muted:#b5b8ba;
  --tab-text:#555;
}
*{margin:0;padding:0;box-sizing:border-box}
html,body{width:1200px;height:969px;overflow:hidden;background:var(--page)}
body{position:relative;font-family:"PT Sans",sans-serif;color:var(--ink)}
.abs{position:absolute}

.brand{left:126px;top:36px;font-family:"PT Sans",sans-serif;font-size:34px;font-weight:700;color:var(--blue);display:flex;align-items:center;gap:8px}
.brand-mark{width:14px;height:14px;border-radius:50%;background:var(--blue)}
.main-nav{left:776px;top:73px;display:flex;gap:17px;font-family:"Noto Serif",serif;font-size:13.5px;text-transform:uppercase}
.main-nav a{color:#111;text-decoration:none}
.main-nav a.active{color:var(--blue)}

.search-bar{left:126px;top:115px;width:948px;height:40px;background:var(--bar);display:flex;align-items:center;color:#fff;font-size:13px}
.search-title{margin-left:29px;font-size:17px;margin-right:15px}
.radio{display:flex;align-items:center;gap:5px;margin-right:10px}
.radio i{width:13px;height:13px;border-radius:50%;background:#fff;display:block}
.radio i.on{border:3px solid #fff;background:var(--blue);box-shadow:0 0 0 1px #888}
.select{width:166px;height:22px;background:#fff;color:#222;border-radius:2px;margin-left:8px;padding:0 7px;display:flex;align-items:center;justify-content:space-between;font-size:12.5px}
.select:first-of-type{margin-left:8px}
.btn-search{margin-left:8px;height:22px;padding:0 11px;background:var(--blue-light);border:1px solid #5fcaf3;font-family:"Noto Serif",serif;font-size:11.5px;display:flex;align-items:center}

.age-tabs{left:126px;top:155px;width:948px;height:40px;display:flex}
.age-tabs li{list-style:none;flex:1;text-align:center;font-family:"Roboto Condensed",sans-serif;font-size:12.5px;color:var(--tab-text);padding-top:11px;border-bottom:5px solid var(--c)}

.section-title{font-family:"Roboto Condensed",sans-serif;font-weight:300;font-size:23px;color:#444;top:222px}

.featured{left:126px;top:259px;width:639px;height:372px;background:radial-gradient(ellipse at 75% 30%,#3b352d,#1d1b19 60%,#141312);overflow:hidden}
.featured-shade{inset:0;background:linear-gradient(90deg,rgba(10,20,25,.45),rgba(0,0,0,0))}
.feat-name{left:55px;top:101px;display:flex;align-items:baseline;gap:8px;color:#ddd}
.feat-name h3{font-weight:400;font-size:20.5px;color:var(--blue);margin-right:4px}
.feat-name .new{font-size:16px;font-family:"Roboto Condensed",sans-serif;font-weight:300}
.feat-name .new small{font-size:12.5px}
.feat-text{left:55px;top:136px;width:265px;font-size:11px;line-height:15.7px;color:#e6e6e6}
.meta{left:55px;top:218px;display:flex;gap:20px;font-size:11px;line-height:13px;color:#fff}
.meta div{display:flex;gap:8px;align-items:center}
.meta span{display:block;color:#8b8f91}
.map-box{left:387px;top:91px;width:206px;height:139px;border-radius:3px;background:#ece8df}
.btn-details{left:446px;top:239px;width:76px;height:25px;background:var(--blue);border:1px solid #7dd3f5;border-radius:2px;color:#111;font-family:"Noto Serif",serif;font-size:12.5px;display:flex;align-items:center;justify-content:center}

.recent{left:770px;top:259px;width:304px;height:372px;background:linear-gradient(90deg,#7d0d12 0%,#b51c22 35%,#d9d2cf 60%,#a9aaa9 100%);overflow:hidden}
.badge{right:0;top:0;width:106px;height:31px;background:var(--blue-light);display:flex;align-items:center;justify-content:center;gap:7px;font-size:14px;color:#111}
.recent-panel{left:0;top:246px;width:304px;height:126px;background:rgba(10,10,10,.88);color:#fff;padding:14px 22px}
.recent-panel h3{font-weight:400;font-size:19px;margin-bottom:5px}
.recent-panel p{font-size:10.5px;line-height:15.5px;color:#e5e5e5}
.recent-links{display:flex;gap:15px;margin-top:10px;font-size:16px;font-weight:400}
.recent-links div{display:flex;align-items:center;gap:8px}

.footer{left:127px;top:670px;width:948px;height:271px;background:var(--footer);border-top:5px solid var(--blue)}
.footer h4{position:absolute;top:38px;font-family:"Noto Serif",serif;font-weight:400;font-size:12.5px;color:var(--blue);letter-spacing:.2px}
.footer ul{position:absolute;top:67px;list-style:none;font-size:9.6px;line-height:15.9px;color:var(--muted)}
.footer .about{position:absolute;left:634px;top:68px;width:292px;font-size:11.3px;line-height:15.9px;color:#d8d8d8}
.copyright{left:0;bottom:0;width:948px;height:46px;background:var(--footer-base);color:#8e9193;font-size:10.5px;display:flex;align-items:center;justify-content:center}
</style>
</head>
<body>

<header>
  <div class="abs brand"><span class="brand-mark"></span>fernlodgings.net</div>
  <nav class="abs main-nav">
    <a class="active" href="#">Home</a><a href="#">About Us</a><a href="#">Hotels</a><a href="#">Contact Us</a>
  </nav>
</header>

<form class="abs search-bar">
  <span class="search-title">Search Hotels :</span>
  <span class="radio"><i></i>All</span>
  <span class="radio"><i class="on"></i>Custom Search</span>
  <span class="select">Location<svg width="12" height="7"><path d="M1 1l5 5 5-5" fill="none" stroke="#444"/></svg></span>
  <span class="select">Age<svg width="12" height="7"><path d="M1 1l5 5 5-5" fill="none" stroke="#444"/></svg></span>
  <span class="select">Style<svg width="12" height="7"><path d="M1 1l5 5 5-5" fill="none" stroke="#444"/></svg></span>
  <span class="btn-search">SEARCH</span>
</form>

<ul class="abs age-tabs">
  <li style="--c:#7a7a7a">1 months</li>
  <li style="--c:#cfcfcf">1-3 months</li>
  <li style="--c:#ababab">3-6 months</li>
  <li style="--c:#d4d4d4">1 year</li>
  <li style="--c:#777">3 years</li>
  <li style="--c:#d0d0d0">3-6 years</li>
  <li style="--c:#8a8a8a">6-10 years</li>
  <li style="--c:#666">15 years</li>
  <li style="--c:#3e3e3e">30 years</li>
  <li style="--c:#a8a8a8">Older</li>
</ul>

<h2 class="abs section-title" style="left:125px">Featured Hotels</h2>
<h2 class="abs section-title" style="left:770px">Recently Added</h2>

<section class="abs featured" role="img" aria-label="Dim hotel suite with sofa, window and fruit bowl">
  <div class="abs featured-shade"></div>
  <div class="abs feat-name">
    <h3>Hotel Name</h3>
    <svg width="20" height="19" viewBox="0 0 24 23"><path d="M12 1l3.3 7 7.7.8-5.8 5.2 1.7 7.6L12 17.7 5.1 21.6l1.7-7.6L1 8.8 8.7 8z" fill="#f6b92b"/></svg>
    <span class="new">NEW <small>[ 1 month ]</small></span>
  </div>
  <p class="abs feat-text">Lorem ipsum dolor sit amet, consectetur adipiscing elit. Sed id tempus enim. Etiam eros velit, rutrum in fringilla id, fermentum sit amet nulla. Nullam cursus ut lorem commodo eu pharetra elit blandit.</p>
  <div class="abs meta">
    <div><svg width="12" height="17" viewBox="0 0 12 17"><path d="M6 0a6 6 0 016 6c0 4-6 11-6 11S0 10 0 6a6 6 0 016-6z" fill="#fff"/><circle cx="6" cy="6" r="2.3" fill="#222"/></svg><p>Location<span>New York</span></p></div>
    <div><svg width="12" height="16" viewBox="0 0 12 16"><path d="M1 1h10M1 15h10M2 1c0 5 8 5 8 14M10 1c0 5-8 5-8 14" fill="none" stroke="#fff" stroke-width="1.4"/></svg><p>Age<span>1 month</span></p></div>
    <div><svg width="13" height="16" viewBox="0 0 13 16"><path d="M1 1h11L6.5 8zM6.5 8v7M3 15h7" fill="none" stroke="#fff" stroke-width="1.4"/></svg><p>Style<span>Lorem ipsum</span></p></div>
  </div>
  <div class="abs map-box" role="img" aria-label="Street map showing the hotel location"></div>
  <div class="abs btn-details">DETAILS</div>
</section>

<section class="abs recent" role="img" aria-label="Restaurant table set with wine glasses before red curtains">
  <div class="abs badge">
    <svg width="18" height="17" viewBox="0 0 24 23"><path d="M12 1l3.3 7 7.7.8-5.8 5.2 1.7 7.6L12 17.7 5.1 21.6l1.7-7.6L1 8.8 8.7 8z" fill="#f6b92b"/></svg>1 Months
  </div>
  <div class="abs recent-panel">
    <h3>Hotel Name</h3>
    <p>Lorem ipsum dolor sit amet, consectetur adipiscing elit. id tempus enim. Etiam eros velit,</p>
    <div class="recent-links">
      <div><svg width="25" height="25" viewBox="0 0 25 25"><circle cx="12.5" cy="12.5" r="12.5" fill="var(--blue)"/><path d="M12.5 5a4.5 4.5 0 014.5 4.5c0 3.2-4.5 9.5-4.5 9.5S8 12.7 8 9.5A4.5 4.5 0 0112.5 5z" fill="#111"/><circle cx="12.5" cy="9.5" r="1.7" fill="var(--blue)"/></svg>Map</div>
      <div><svg width="25" height="25" viewBox="0 0 25 25"><circle cx="12.5" cy="12.5" r="12.5" fill="var(--blue)"/><rect x="6.5" y="8" width="12" height="9" rx="1" fill="none" stroke="#111" stroke-width="1.6"/><path d="M8 16l3.5-4 2.5 2.5 1.5-1.5 2 3z" fill="#111"/></svg>Image</div>
    </div>
  </div>
</section>

<footer class="abs footer">
  <h4 style="left:21px">HOTELS BY LOCATION</h4>
  <ul style="left:21px"><li>Abu Dhabi</li><li>Auckland</li><li>Bangkok</li><li>Cape Town</li><li>Dubai</li><li>Florida</li><li>Goa</li><li>Hongkong</li></ul>
  <ul style="left:141px"><li>Istanbul</li><li>Lisbon</li><li>London</li><li>Madrid</li><li>Manchester</li><li>Milan</li><li>Moscow</li><li>New york</li></ul>
  <ul style="left:270px"><li>Paris</li><li>Rio de Janeiro</li><li>Singapore</li><li>Sydney</li><li>Thailand</li><li>Tokyo</li><li>Venis</li><li>Zurich</li></ul>
  <h4 style="left:418px">HOTELS BY AGE</h4>
  <ul style="left:418px"><li>1 year</li><li>1-5 years</li><li>5-10 years</li><li>10-15 years</li><li>15-30 years</li><li>30-60 years</li><li>60-100 years</li><li>More than 100 years</li></ul>
  <h4 style="left:634px">ABOUT FERN LODGINGS.NET</h4>
  <p class="about">Lorem ipsum dolor sit amet, consectetur adipiscing elit. Sed id tempus enim. Etiam eros velit, rutrum in fringilla id, fermentum sit amet nulla. Nullam cursus mi ut lorem commodo eu pharetra elit blandit. Phasellus malesuada, massa et adipiscing tempor, tellus lacus vulputate dui, non commodo mi neque a dui. Praesent enim dolor,</p>
  <div class="abs copyright">© Copyright 2013. All Rights Reserved</div>
</footer>

</body>
</html>
```